Construction Company Business Card

Business Card Design using new Logo

Contact Information for Business Card

include all company info and website

Requirements
Must have
• Wesley Corman - President
ph. 254-617-0382
Cedar Knoll, TX
wesley@ironmarkframing.com
www.ironmarkframing.com

```html
<!DOCTYPE html>
<html lang="en">
<head>
<meta charset="utf-8">
<title>Ironmark Framing – Business Card</title>
<link href="https://fonts.googleapis.com/css2?family=Lato:wght@400;700&display=swap" rel="stylesheet">
<style>
  :root {
    --stage: #3a3a3a;
    --card: #000000;
    --red: #c8222a;
    --silver: #c9c9cc;
  }
  * { box-sizing: border-box; margin: 0; padding: 0; }
  html, body { width: 1200px; height: 1200px; overflow: hidden; }
  body {
    background: var(--stage);
    font-family: "Lato", Arial, sans-serif;
    position: relative;
  }
  .card {
    position: absolute;
    left: 171px;
    width: 846px;
    height: 482px;
    background: var(--card);
    border-radius: 18px;
    overflow: hidden;
  }
  .card-front { top: 94px; }
  .card-back { top: 612px; height: 484px; }

  .wave-area {
    position: absolute; left: 0; right: 0; bottom: 0; height: 122px;
    background: linear-gradient(180deg, rgba(200,34,42,0) 0%, rgba(200,34,42,0.55) 35%, var(--red) 75%);
  }

  .holder { position: absolute; left: 29px; top: 70px; }
  .holder-name { color: var(--red); font-weight: 700; font-size: 29px; line-height: 1.1; }
  .holder-title { color: var(--silver); font-weight: 700; font-size: 21px; letter-spacing: 0.5px; margin-top: 2px; }
  .holder-rule { width: 106px; height: 3px; background: var(--red); margin-top: 24px; }

  .contacts { position: absolute; left: 29px; top: 180px; list-style: none; }
  .contacts li {
    display: flex; align-items: center; gap: 11px;
    color: var(--red); font-weight: 700; font-size: 22px;
    height: 34px; letter-spacing: 0.3px;
  }
  .contacts svg { width: 21px; height: 21px; flex: none; }

  .brand {
    position: absolute;
    display: flex; align-items: center; gap: 12px;
    color: var(--silver); font-weight: 700;
    letter-spacing: 2px; text-transform: uppercase; white-space: nowrap;
  }
  .brand-mark { background: var(--red); flex: none; }
  .card-front .brand { right: 30px; top: 150px; font-size: 30px; }
  .card-front .brand-mark { width: 14px; height: 14px; }
  .card-back .brand { left: 50%; top: 186px; transform: translateX(-50%); font-size: 46px; gap: 18px; }
  .card-back .brand-mark { width: 20px; height: 20px; }

  .location {
    position: absolute; right: 30px; top: 322px;
    color: var(--red); font-weight: 700; font-size: 22px; letter-spacing: 0.3px;
  }

  .back-site {
    position: absolute; left: 30px; right: 30px; top: 420px;
    display: flex; align-items: center; gap: 10px;
    color: var(--silver); font-weight: 700; font-size: 27px; letter-spacing: 0.5px;
  }
  .back-site .line { flex: 1; height: 2px; background: linear-gradient(90deg, transparent, var(--red)); }
  .back-site .line.right { background: linear-gradient(90deg, var(--red), transparent); }
</style>
</head>
<body>

<section class="card card-front">
  <div class="wave-area" role="img" aria-label="Red and silver sweeping wave decoration along the bottom of the card"></div>

  <div class="holder">
    <h1 class="holder-name">Wesley Corman</h1>
    <p class="holder-title">President</p>
    <div class="holder-rule"></div>
  </div>

  <ul class="contacts">
    <li>
      <svg viewBox="0 0 24 24" fill="var(--silver)"><path d="M6.6 10.8a15 15 0 0 0 6.6 6.6l2.2-2.2c.3-.3.7-.4 1-.2 1.1.4 2.3.6 3.6.6.6 0 1 .4 1 1V20c0 .6-.4 1-1 1A17 17 0 0 1 3 4c0-.6.4-1 1-1h3.5c.6 0 1 .4 1 1 0 1.3.2 2.5.6 3.6.1.3 0 .7-.2 1z"/></svg>
      254-617-0382
    </li>
    <li>
      <svg viewBox="0 0 24 24" fill="var(--silver)"><path d="M2 5h20v14H2z"/><path d="M2 5l10 8 10-8" fill="none" stroke="#000" stroke-width="1.6"/></svg>
      wesley@ironmarkframing.com
    </li>
    <li>
      <svg viewBox="0 0 24 24"><circle cx="12" cy="12" r="10" fill="var(--silver)"/><path d="M2 12h20M12 2c3 3 3 17 0 20M12 2c-3 3-3 17 0 20" fill="none" stroke="#000" stroke-width="1.4"/></svg>
      www.ironmarkframing.com
    </li>
  </ul>

  <div class="brand"><span class="brand-mark"></span>Ironmark Framing</div>

  <p class="location">Cedar Knoll, TX</p>
</section>

<section class="card card-back">
  <div class="brand"><span class="brand-mark"></span>Ironmark Framing</div>
  <div class="back-site">
    <span class="line"></span>
    www.ironmarkframing.com
    <span class="line right"></span>
  </div>
</section>

</body>
</html>
```